Redesign of TaskHarbor.com website

Our website was initially developed 6+ years ago and has been maintained by several different designers. As a result, it is overly complex, inconsistent format/layout and the content is not well structured/easy to navigate

We need the site redeveloped with a more modern look and feel, simpler content structure and ability to implement new/improved tools, such as: Dynamic Forms, Sales Funnels, Landing Pages, improved metadata of our pages and posts, improved SEO/Page ranking, etc.

We currently use DealRiver CRM, Steady Reach for marketing automation and GridPilot forms. We are investigating Floxen for workflow integration which could extend to our website.

Our current website is developed in WordPress, ideally we will stick with this platform, but we’re happy to consider other CMS' if strongly recommended. We may decide to remove/consolidate some of the pages and/or content as part of this re-design.

We don't want to rebrand (ie change corporate logo, colours scheme etc) as part of this website redevelopment and it is critical that we don't lose our current Page Ranking, SEO rankings, backlink benefits, etc as part of this redevelopment.

Sites we like the feel/design of are: boardwiley.com, tallypoint.com and rankgrove.com

Target Market(s)

Corporate, Enterprise and Government B2B clients.

Coding

Coded - Design and coding required

Number of Pages Required

5+ page

Font styles to use
Sans Serif

Colors
ffffff
ec1f27

Requirements
Must have
• Must retain the majority of content on our existing website (although we may re-write some of it as part of this redesign process).
Nice to have
• See above "Project Description"
Should not have

```html
<!DOCTYPE html>
<html lang="en">
<head>
<meta charset="utf-8">
<title>Blog – TaskHarbor</title>
<link href="https://fonts.googleapis.com/css2?family=Poppins:wght@400;500;600;700&family=Montserrat:wght@600;700;800&display=swap" rel="stylesheet">
<style>
:root{
  --red:#ec1f27;
  --white:#ffffff;
  --ink:#1d1d1d;
  --body:#4a4a4a;
  --dark:#232323;
  --footer-text:#c9c9c9;
}
*{box-sizing:border-box;margin:0;padding:0}
html,body{width:715px;height:1200px;overflow:hidden;background:var(--white)}
body{position:relative;font-family:'Poppins',sans-serif;color:var(--ink)}

.hero{position:absolute;left:0;top:0;width:715px;height:280px;
  background:linear-gradient(180deg,#4b5872 0%,#3a3f4f 40%,#3d3326 75%,#2c2620 100%)}
.hero-shape{position:absolute;left:0;top:0}
.hero-title{position:absolute;top:126px;width:100%;text-align:center;color:var(--white);
  font-family:'Montserrat',sans-serif;font-weight:800;font-size:30px;letter-spacing:1px}
.scroll-hint{position:absolute;left:351px;top:196px;width:12px;height:18px;border:1.5px solid var(--white);border-radius:7px}
.scroll-hint::after{content:"";position:absolute;left:4px;top:3px;width:1.5px;height:4px;background:var(--white)}

.site-header{position:absolute;left:53px;top:16px;width:609px;height:44px;background:var(--white)}
.brand{position:absolute;left:12px;top:12px;display:flex;align-items:center;gap:5px}
.brand-dot{width:12px;height:12px;border-radius:50%;background:var(--red)}
.brand-name{font-size:14px;font-weight:500;color:var(--red)}
.topbar{position:absolute;right:0;top:0;width:350px;height:15px;background:var(--red);
  clip-path:polygon(0 0,100% 0,100% 100%,4% 100%);display:flex;align-items:center;
  padding-left:20px;gap:10px;font-size:6px;color:var(--white)}
.topbar .icon{width:6px;height:6px;fill:var(--white);vertical-align:-1px;margin-right:2px}
.socials{margin-left:auto;margin-right:12px;display:flex;gap:6px}
.socials span{width:6px;height:6px;border-radius:50%;background:var(--white)}
.nav{position:absolute;right:24px;top:24px;display:flex;gap:15px;font-size:7.5px;font-weight:500}
.nav .active{color:var(--red)}

.news-title{position:absolute;top:310px;width:100%;text-align:center;font-family:'Montserrat',sans-serif;font-weight:700;font-size:19px}
.filters{position:absolute;top:338px;width:100%;display:flex;justify-content:center;gap:19px;font-size:9px}
.filters .active{color:var(--red)}

.card{position:absolute;width:186px;height:242px;background:var(--white);box-shadow:0 6px 14px rgba(0,0,0,.1)}
.card-media{height:121px}
.card-body{padding:13px 11px 0 13px}
.card-title{font-family:'Montserrat',sans-serif;font-weight:700;font-size:8px;line-height:10.5px;margin-bottom:5px}
.card-text{font-size:7.3px;line-height:10px;color:var(--body)}
.read-more{display:block;margin-top:4px;font-family:'Montserrat',sans-serif;font-weight:700;font-size:7.5px;color:var(--red);letter-spacing:.3px}

.load-more{position:absolute;left:321px;top:885px;width:73px;height:18px;background:var(--red);
  clip-path:polygon(0 0,100% 0,88% 100%,0 100%);color:var(--white);font-family:'Montserrat',sans-serif;font-weight:700;font-size:7px;display:flex;align-items:center;padding-left:13px}

.footer-shape{position:absolute;left:0;top:930px}
.world-map{position:absolute;left:490px;top:1040px;width:170px;height:100px;background:radial-gradient(ellipse,rgba(255,255,255,.06),rgba(255,255,255,0) 70%)}
.footer-brand{position:absolute;left:54px;top:1073px;display:flex;align-items:center;gap:5px}
.footer-col{position:absolute;top:1025px;font-size:7.5px;color:var(--footer-text)}
.footer-col h3{font-family:'Montserrat',sans-serif;font-weight:700;font-size:9px;color:var(--white);margin-bottom:5px}
.footer-col li{list-style:none;line-height:13.8px}
.newsletter-input{margin-top:6px;width:126px;height:18px;background:#333;color:#aaa;font-size:6.5px;padding:5px 8px}
.subscribe{margin-top:4px;width:62px;height:18px;background:var(--red);clip-path:polygon(0 0,100% 0,88% 100%,0 100%);
  color:var(--white);font-family:'Montserrat',sans-serif;font-weight:700;font-size:7px;padding:5px 9px}
.contact-list li{display:flex;gap:4px;align-items:flex-start}
.contact-list svg{width:7px;height:7px;fill:var(--red);flex:none;margin-top:3px}
.footer-rule{position:absolute;left:53px;top:1170px;width:609px;height:1px;background:#444}
.footer-bottom{position:absolute;left:53px;top:1180px;width:609px;display:flex;font-size:7.5px;color:var(--white)}
.legal{margin-left:auto;display:flex;gap:9px}
.to-top{position:absolute;left:671px;top:1162px;width:19px;height:19px;border-radius:50%;background:var(--red)}
.to-top svg{position:absolute;left:6px;top:6px}
</style>
</head>
<body>

<section class="hero" role="img" aria-label="City skyline at dusk beside the harbour">
  <svg class="hero-shape" width="715" height="280" viewBox="0 0 715 280">
    <polygon points="424,242 715,217 715,268" fill="#ec1f27"/>
    <polygon points="0,280 424,242 715,268 715,280" fill="#ffffff"/>
  </svg>
  <h1 class="hero-title">BLOG</h1>
  <span class="scroll-hint"></span>
</section>

<header class="site-header">
  <div class="brand"><span class="brand-dot"></span><span class="brand-name">taskharbor</span></div>
  <div class="topbar">
    <span><svg class="icon" viewBox="0 0 10 10"><path d="M2 0l2 2-1 1.5c.8 1.5 2 2.7 3.5 3.5L8 6l2 2-1.5 2C4 10 0 6 0 1.5z"/></svg>Contact Us on 1300 TH DESK</span>
    <span><svg class="icon" viewBox="0 0 10 8"><path d="M0 0h10v1L5 4 0 1zM0 2l5 3 5-3v6H0z"/></svg>info@taskharbor.com</span>
    <div class="socials"><span></span><span></span><span></span><span></span><span></span></div>
  </div>
  <nav class="nav">
    <span>Home</span><span>Services</span><span>About</span><span>Clients</span><span>Resources</span><span class="active">Blog</span><span>Contact</span>
    <svg width="8" height="8" viewBox="0 0 10 10"><circle cx="4" cy="4" r="3" fill="none" stroke="#1d1d1d" stroke-width="1.4"/><path d="M6.3 6.3L9 9" stroke="#1d1d1d" stroke-width="1.4"/></svg>
  </nav>
</header>

<h2 class="news-title">The Latest News &amp; Information</h2>
<div class="filters"><span class="active">View all</span><span>Business Continuity</span><span>Disaster Recovery</span><span>Pandemic</span></div>

<article class="card" style="left:71px;top:371px">
  <div class="card-media" role="img" aria-label="Businessman using a tablet against a city backdrop" style="background:linear-gradient(135deg,#c9c3b8,#5d6f88 60%,#24344e)"></div>
  <div class="card-body"><h3 class="card-title">How's Your User Experience for Your Disaster Recovery?</h3>
  <p class="card-text">It may sound strange to talk about “touchy-feely” stuff like user experience in the context of IT disaster recovery. After all, the priority is on getting systems up and running again within …</p><span class="read-more">READ MORE</span></div>
</article>
<article class="card" style="left:265px;top:371px">
  <div class="card-media" role="img" aria-label="Hand writing adapt to changes in a notebook beside a keyboard" style="background:linear-gradient(135deg,#c7a57c,#eeeeee 50%,#d8d8d8)"></div>
  <div class="card-body"><h3 class="card-title">Adapt or Die – A Darwinian Take on Business Continuity</h3>
  <p class="card-text">Most businesses experience change constantly. Markets, technologies, regulations and strategies all evolve. Enterprises that stand still get left behind and disappear, one way or another…</p><span class="read-more">READ MORE</span></div>
</article>
<article class="card" style="left:459px;top:371px">
  <div class="card-media" role="img" aria-label="Keyboard with a green recovery key" style="background:linear-gradient(135deg,#e4e4e4,#cfcfcf 45%,#7cc35a 75%,#e8e8e8)"></div>
  <div class="card-body"><h3 class="card-title">Why Stop at Just Disaster Recovery with Your DRP?</h3>
  <p class="card-text">Do more with less. Who hasn't already heard that in business? And just because something – like disaster recovery planning and management – is vital to ensuring enterprise survival …</p><span class="read-more">READ MORE</span></div>
</article>

<article class="card" style="left:71px;top:627px">
  <div class="card-media" role="img" aria-label="Black and white close-up of office equipment" style="background:linear-gradient(135deg,#1e1e1e,#6b6b6b 50%,#2a2a2a)"></div>
  <div class="card-body"><h3 class="card-title">How's Your User Experience for Your Disaster Recovery?</h3>
  <p class="card-text">It may sound strange to talk about “touchy-feely” stuff like user experience in the context of IT disaster recovery. After all, the priority is on getting systems up and running again within …</p><span class="read-more">READ MORE</span></div>
</article>
<article class="card" style="left:265px;top:627px">
  <div class="card-media" role="img" aria-label="Hands being washed under a tap" style="background:linear-gradient(135deg,#7d7e7a,#b6b2aa 50%,#8a8a86)"></div>
  <div class="card-body"><h3 class="card-title">Adapt or Die – A Darwinian Take on Business Continuity</h3>
  <p class="card-text">Most businesses experience change constantly. Markets, technologies, regulations and strategies all evolve. Enterprises that stand still get left behind and disappear, one way or another…</p><span class="read-more">READ MORE</span></div>
</article>
<article class="card" style="left:459px;top:627px">
  <div class="card-media" role="img" aria-label="Car driving on a circuit board road" style="background:linear-gradient(160deg,#dfe8f5,#3f6fc4 40%,#1f3f8f)"></div>
  <div class="card-body"><h3 class="card-title">Why Stop at Just Disaster Recovery with Your DRP?</h3>
  <p class="card-text">Do more with less. Who hasn't already heard that in business? And just because something – like disaster recovery planning and management – is vital to ensuring enterprise survival …</p><span class="read-more">READ MORE</span></div>
</article>

<span class="load-more">LOAD MORE</span>

<svg class="footer-shape" width="715" height="270" viewBox="0 0 715 270">
  <polygon points="0,18 265,42 0,65" fill="#ec1f27"/>
  <polygon points="0,65 265,42 715,3 715,270 0,270" fill="#232323"/>
</svg>
<div class="world-map" role="img" aria-label="Faint dotted world map"></div>

<footer>
  <div class="footer-brand"><span class="brand-dot"></span><span class="brand-name">taskharbor</span></div>
  <div class="footer-col" style="left:198px">
    <h3>Useful Links</h3>
    <ul><li>Home</li><li>Services</li><li>About</li><li>Clients</li><li>Resources</li><li>Blog</li><li>Contact</li></ul>
  </div>
  <div class="footer-col" style="left:322px">
    <h3>Newsletter</h3>
    <p>Subscribe to our newsletter</p>
    <div class="newsletter-input">Email address</div>
    <div class="subscribe">SUBSCRIBE</div>
  </div>
  <div class="footer-col" style="left:499px">
    <h3>Contact Us</h3>
    <ul class="contact-list">
      <li><svg viewBox="0 0 10 10"><path d="M2 0l2 2-1 1.5c.8 1.5 2 2.7 3.5 3.5L8 6l2 2-1.5 2C4 10 0 6 0 1.5z"/></svg>Contact Us on 1300 TH DESK</li>
      <li><svg viewBox="0 0 10 8"><path d="M0 0h10v1L5 4 0 1zM0 2l5 3 5-3v6H0z"/></svg>info@taskharbor.com</li>
      <li style="line-height:9.5px;margin-top:3px"><svg viewBox="0 0 10 10"><path d="M5 0a3.5 3.5 0 0 1 3.5 3.5C8.5 6 5 10 5 10S1.5 6 1.5 3.5A3.5 3.5 0 0 1 5 0zm0 2a1.5 1.5 0 1 0 0 3 1.5 1.5 0 0 0 0-3z"/></svg><span>Level 12, Harbour Point, 88 Kent<br>Street, Sydney NSW 2000 Australia</span></li>
    </ul>
  </div>
  <div class="footer-rule"></div>
  <div class="footer-bottom">
    <span>Copyright © 2021 TaskHarbor | All Rights Reserved</span>
    <div class="legal"><span>Privacy</span><span>Disclaimer</span><span>Spam Policy</span><span>Sitemap</span></div>
  </div>
  <span class="to-top"><svg width="7" height="7" viewBox="0 0 10 10"><path d="M1 7l4-4 4 4" fill="none" stroke="#fff" stroke-width="1.6"/></svg></span>
</footer>

</body>
</html>
```